New bussiness card, using company logo.
Lachlan Voss
Manager/Director
Birch Property Developments
Po Box 4657
Thuringowa Central
Qld
0455 386 218
lachlan@birchpropertydevelopments
eye catching, vibrant colours, professional

```html
<!DOCTYPE html>
<html lang="en">
<head>
<meta charset="utf-8">
<title>Lachlan Voss – Birch Property Developments</title>
<link rel="stylesheet" href="https://fonts.googleapis.com/css2?family=Lato:wght@400;700;900&display=swap">
<style>
  :root {
    --brand-red: #e0242f;
    --paper: #ffffff;
    --ink-light: #ffffff;
    --logo-red: #d9222c;
  }
  * { margin: 0; padding: 0; box-sizing: border-box; }
  html, body {
    width: 960px;
    height: 1200px;
    overflow: hidden;
    background: var(--paper);
  }
  .card {
    position: relative;
    width: 960px;
    height: 1200px;
    background: var(--paper);
    font-family: "Lato", sans-serif;
  }
  .card__details {
    position: absolute;
    left: 0;
    top: 0;
    width: 960px;
    height: 909px;
    background: var(--brand-red);
    color: var(--ink-light);
    text-align: center;
  }
  .card__name {
    position: absolute;
    top: 150px;
    width: 100%;
    font-weight: 900;
    font-size: 88px;
    letter-spacing: 8px;
    line-height: 1;
    text-transform: uppercase;
  }
  .card__role {
    position: absolute;
    top: 252px;
    width: 100%;
    font-weight: 700;
    font-size: 58px;
    letter-spacing: 1px;
    line-height: 1;
  }
  .card__contact {
    position: absolute;
    top: 393px;
    width: 100%;
    font-weight: 400;
    font-size: 54px;
    line-height: 74px;
  }
  .card__email {
    position: absolute;
    top: 690px;
    width: 100%;
    font-weight: 400;
    font-size: 50px;
    line-height: 1;
  }
  .card__brand {
    position: absolute;
    left: 0;
    top: 909px;
    width: 960px;
    height: 291px;
    padding-top: 24px;
    display: flex;
    align-items: center;
    justify-content: center;
    gap: 20px;
  }
  .brand__mark {
    width: 36px;
    height: 36px;
    background: var(--logo-red);
  }
  .brand__name {
    font-family: "Lato", sans-serif;
    font-weight: 900;
    font-size: 44px;
    color: var(--logo-red);
    text-transform: uppercase;
    letter-spacing: 1px;
  }
</style>
</head>
<body>
  <main class="card">
    <section class="card__details">
      <h1 class="card__name">Lachlan Voss</h1>
      <p class="card__role">Manager/Director</p>
      <p class="card__contact">
        Po Box 4657<br>
        Harrowvale Central NSW<br>
        0455 386 218
      </p>
      <p class="card__email">lachlan@birchpropertydevelopments</p>
    </section>
    <footer class="card__brand">
      <span class="brand__mark" aria-hidden="true"></span>
      <span class="brand__name">Birch Property Developments</span>
    </footer>
  </main>
</body>
</html>
```